Brenmoor Group needs a business card

I would like the card to be simple but modern and elegant.
I like black and white.
or black and gold.
we are a private finance lender and also are involved in property and property developments.

please look at the business card photos i provided i would like B.G only one one side and all the other details on the other side use fonts that tie in with my theme.

Industry/Entity Type

Finance

Contact Information for Business Card

Brenmoor Group (B.G) Callum Brenmoor M: 0418396152 E: callumbren@quivomail.com

Font styles to use
Other font styles liked:
• Use fonts that would reflect our business

Colors
000000
ffffff

Requirements
Must have
• one side of details
• other side has either B.G or Brenmoor Group like in the photos provided

```html
<!DOCTYPE html>
<html lang="en">
<head>
<meta charset="utf-8">
<title>Brenmoor Group — Business Card</title>
<link rel="stylesheet" href="https://fonts.googleapis.com/css2?family=Roboto+Condensed:wght@400;700&display=swap">
<style>
  :root {
    --backdrop: #cfc8bd;
    --card-black: #03040a;
    --card-white: #ffffff;
    --ink: #111111;
    --ink-reverse: #ffffff;
  }
  * { margin: 0; padding: 0; box-sizing: border-box; }
  html, body {
    width: 1200px;
    height: 1200px;
    overflow: hidden;
  }
  body {
    position: relative;
    background: var(--backdrop);
    font-family: "Roboto Condensed", "Arial Narrow", sans-serif;
    color: var(--ink);
  }
  .card {
    position: absolute;
    width: 692px;
    height: 390px;
  }
  .card--front {
    left: 254px;
    top: 185px;
    background: var(--card-black);
    display: flex;
    align-items: center;
    justify-content: center;
  }
  .monogram {
    color: var(--ink-reverse);
    font-weight: 700;
    font-size: 104px;
    letter-spacing: -4px;
    line-height: 1;
    margin-top: 14px;
  }
  .card--back {
    left: 256px;
    top: 624px;
    background: var(--card-white);
  }
  .company-name {
    position: absolute;
    top: 18px;
    right: 26px;
    font-weight: 700;
    font-size: 30px;
    line-height: 1.2;
  }
  .holder-name {
    position: absolute;
    left: 41px;
    top: 276px;
    font-weight: 700;
    font-size: 20px;
    letter-spacing: 0.3px;
    line-height: 1.2;
  }
  .holder-rule {
    position: absolute;
    left: 41px;
    top: 307px;
    width: 63px;
    height: 1.5px;
    background: var(--ink);
  }
  .contact {
    position: absolute;
    top: 331px;
    display: flex;
    align-items: center;
    gap: 7px;
    font-size: 18px;
    line-height: 1.2;
  }
  .contact--phone { left: 41px; }
  .contact--email { left: 235px; }
  .contact svg { display: block; }
</style>
</head>
<body>
  <section class="card card--front" aria-label="Card front">
    <div class="monogram">B.G</div>
  </section>

  <section class="card card--back" aria-label="Card back">
    <div class="company-name">Brenmoor Group</div>
    <div class="holder-name">Callum Brenmoor</div>
    <div class="holder-rule"></div>
    <div class="contact contact--phone">
      <svg width="10" height="16" viewBox="0 0 10 16" aria-hidden="true">
        <rect x="1" y="1" width="8" height="14" rx="1.2" fill="none" stroke="#111" stroke-width="1.8"/>
        <line x1="3.5" y1="12.3" x2="6.5" y2="12.3" stroke="#111" stroke-width="1.4"/>
      </svg>
      <span>0418396152</span>
    </div>
    <div class="contact contact--email">
      <svg width="20" height="14" viewBox="0 0 20 14" aria-hidden="true">
        <rect x="1" y="1" width="18" height="12" fill="none" stroke="#111" stroke-width="1.6"/>
        <polyline points="1,1 10,8 19,1" fill="none" stroke="#111" stroke-width="1.6"/>
        <line x1="1" y1="13" x2="8" y2="6.5" stroke="#111" stroke-width="1.2"/>
        <line x1="19" y1="13" x2="12" y2="6.5" stroke="#111" stroke-width="1.2"/>
      </svg>
      <span>callumbren@quivomail.com</span>
    </div>
  </section>
</body>
</html>
```